business card for horse saddlery

after a new business card for our saddlery, i will add 2 logos we have previously used and they can be used (or not) . Any images can be used from our website also at www.bramwoods.net.au, I have also added our brand logo, which may be good to incorporate on back ? we have over 15, 000 items online, ship Australia Wide.

Target Market(s)

horse owners

Industry/Entity Type

Retail - Equestrian

Contact Information for Business Card

Bramwood Horse Supplies, 1300 62 48 07, www.bramwoods.net.au, 278 Tallowmere Rd Corrindale Q 4602

Requirements
Must have
• ridelark is our brand so ridelark logo on back as 'distributers of', easy to read
Nice to have
• professional but fun
Should not have
• double sided (description wont save double sided)

```html
<!DOCTYPE html>
<html lang="en">
<head>
<meta charset="utf-8">
<title>Bramwood Horse Supplies – Business Card</title>
<link rel="stylesheet" href="https://fonts.googleapis.com/css2?family=Poppins:ital,wght@0,300;0,400;0,600;0,800;1,300&display=swap">
<style>
  :root {
    --backdrop: #0a3479;
    --card-front: #dedcd7;
    --card-back: #ebeae6;
    --brand-blue: #26478f;
    --ink: #161616;
    --gold: #d9a12c;
    --white: #ffffff;
  }
  * { margin: 0; padding: 0; box-sizing: border-box; }
  html, body {
    width: 1200px; height: 783px; overflow: hidden;
    background: var(--backdrop);
    font-family: "Poppins", sans-serif;
  }
  .canvas {
    position: relative; width: 1200px; height: 783px;
    display: flex; align-items: center; justify-content: center; gap: 50px;
  }
  .card {
    position: relative; width: 500px; height: 286px; overflow: hidden;
    box-shadow: 0 14px 30px rgba(0, 0, 0, 0.35);
  }
  .card-front { background: var(--card-front); }
  .card-back {
    background: var(--card-back);
    display: flex; align-items: center; justify-content: center;
  }

  .company-name {
    position: absolute; left: 26px; top: 22px;
    color: var(--brand-blue); font-weight: 800;
    font-size: 19px; line-height: 0.95; text-transform: uppercase;
  }
  .divider {
    position: absolute; left: 0; top: 92px;
    width: 380px; height: 3px; background: var(--brand-blue);
  }
  .brand-mark {
    position: absolute; right: 26px; top: 62px;
    display: flex; align-items: center; gap: 7px;
  }
  .brand-mark .dot {
    width: 22px; height: 22px; border-radius: 50%; background: var(--gold);
  }
  .brand-mark .word {
    color: var(--brand-blue); font-weight: 600; font-size: 17px;
  }
  .person {
    position: absolute; left: 0; right: 0; top: 118px; text-align: center;
  }
  .person-name {
    color: var(--ink); font-weight: 800; font-size: 34px;
    letter-spacing: 0.5px; text-transform: uppercase; line-height: 1;
  }
  .person-rule {
    width: 46px; height: 2px; background: var(--brand-blue);
    margin: 12px auto 6px;
  }
  .person-title {
    color: var(--ink); font-weight: 300; font-style: italic; font-size: 16px;
  }

  .contact-band {
    position: absolute; left: 0; right: 0; bottom: 0; height: 62px;
    padding: 0 20px;
    background: var(--gold);
    display: flex; align-items: center; justify-content: space-between;
    color: var(--white); font-size: 10px; font-weight: 300; letter-spacing: 0.3px;
  }
  .contact-item { display: flex; align-items: center; gap: 6px; white-space: nowrap; }
  .contact-item svg { width: 12px; height: 12px; flex: none; }
  .contact-sep { width: 1px; height: 24px; background: var(--white); transform: rotate(20deg); flex: none; }

  .distributor-mark { display: flex; align-items: center; gap: 12px; }
  .distributor-mark .square { width: 26px; height: 26px; background: var(--brand-blue); }
  .distributor-mark .word {
    color: var(--brand-blue); font-weight: 400; font-size: 36px;
    letter-spacing: 4px; text-transform: uppercase;
  }
</style>
</head>
<body>
<main class="canvas">
  <section class="card card-front">
    <h1 class="company-name">Bramwood<br>Horse<br>Supplies</h1>
    <div class="divider"></div>
    <div class="brand-mark">
      <span class="dot"></span>
      <span class="word">Bramwood</span>
    </div>
    <div class="person">
      <p class="person-name">Maren Ashcroft</p>
      <div class="person-rule"></div>
      <p class="person-title">Manager</p>
    </div>
    <footer class="contact-band">
      <span class="contact-item">
        <svg viewBox="0 0 16 16"><circle cx="8" cy="8" r="8" fill="#fff"/><path d="M5.4 4.2l1.3 1.6-.7 1c.5 1.1 1.2 1.8 2.3 2.3l1-.7 1.6 1.3-.6 1.3c-3 .2-5.9-2.7-5.7-5.7z" fill="#d9a12c"/></svg>
        1300 62 48 07
      </span>
      <span class="contact-sep"></span>
      <span class="contact-item">
        <svg viewBox="0 0 16 16" fill="none" stroke="#fff" stroke-width="1.2"><circle cx="8" cy="8" r="6.6"/><ellipse cx="8" cy="8" rx="2.8" ry="6.6"/><path d="M1.4 8h13.2M2.5 4.8h11M2.5 11.2h11"/></svg>
        www.bramwoods.net.au
      </span>
      <span class="contact-sep"></span>
      <span class="contact-item">
        <svg viewBox="0 0 16 16"><circle cx="8" cy="8" r="8" fill="#fff"/><path d="M8 3.6a2.8 2.8 0 0 0-2.8 2.8C5.2 8.6 8 12.2 8 12.2s2.8-3.6 2.8-5.8A2.8 2.8 0 0 0 8 3.6z" fill="#d9a12c"/><circle cx="8" cy="6.4" r="1" fill="#fff"/></svg>
        278 Tallowmere Rd Corrindale
      </span>
    </footer>
  </section>

  <section class="card card-back">
    <div class="distributor-mark">
      <span class="square"></span>
      <span class="word">Ridelark</span>
    </div>
  </section>
</main>
</body>
</html>
```